I wish to redesign my webpage http://vantomere.com

Must keep the same wording

SEO in my first priority. Must be Hyper SEO friendly.

Thank you

tomas

Reason: due to end of year holiday I extend 7 days

Please add the social medias on the projects

twitter, fb, instagram, linkedin...

```html
<!DOCTYPE html>
<html lang="fr">
<head>
<meta charset="utf-8">
<title>Vantomere.com – Envoi recommandé de lettres de résiliation</title>
<meta name="description" content="Service d'envoi recommandé de lettres de demandes de résiliation : fiable, simple, rapide et sans se déplacer.">
<link href="https://fonts.googleapis.com/css2?family=Arimo:wght@400;700&display=swap" rel="stylesheet">
<style>
:root{
  --dark:#2b2b2b;
  --darker:#1d1d1d;
  --band:#c4c4c4;
  --panel:#f3f3f3;
  --offer:#d9d9d9;
  --line:#dcdcdc;
  --text:#333;
  --muted:#8a8a8a;
  --white:#fff;
  --orange:#f7a01c;
  --cyan:#1cc0e8;
  --yellow:#f2d21a;
}
*{box-sizing:border-box;margin:0;padding:0}
html,body{width:1200px;height:1000px;overflow:hidden}
body{font-family:"Arimo",Arial,sans-serif;color:var(--text);background:var(--white);position:relative}
a{color:inherit;text-decoration:none}
.abs{position:absolute}
ul{list-style:none}

.site-header{position:absolute;left:0;top:0;width:1200px;height:71px;background:var(--dark)}
.brand{left:293px;top:18px;display:flex;align-items:center;gap:5px;color:var(--yellow);font-weight:700;font-size:16px}
.brand-dot{width:14px;height:14px;border-radius:50%;background:var(--yellow)}
.cart{left:798px;top:6px;font-size:7px;font-weight:700;color:#ddd}
.cart b{color:var(--orange)}
.proceed{left:853px;top:0;width:68px;height:19px;background:#666;color:#bbb;font-size:7px;display:flex;align-items:center;justify-content:center}
.proceed-arrow{left:922px;top:0;width:20px;height:19px;background:var(--orange)}
.main-nav{right:258px;top:51px;font-size:7px;font-weight:700;color:var(--white);white-space:nowrap}
.main-nav a{margin-left:3px}

.services{position:absolute;left:0;top:71px;width:1200px;height:190px;background:var(--band)}
.services h2{left:293px;top:42px;font-size:10px;font-weight:400;color:#333}
.slider-arrows{left:914px;top:42px;display:flex;gap:2px}
.slider-arrows span{width:13px;height:10px;background:#aaa}
.service-tiles{left:293px;top:66px;display:flex;gap:4px}
.service-tiles li{width:105.5px;height:76px;background:var(--white);display:flex;align-items:center;justify-content:center}
.tile-art{width:72px;height:56px;border-radius:4px;background:linear-gradient(135deg,#d8d8d8,#555)}
.price{left:0;width:1200px;top:163px;text-align:center;font-size:12.5px;color:#333}

.promise{position:absolute;left:0;top:261px;width:1200px;height:63px;background:var(--dark)}
.promise h1{left:293px;top:16px;color:var(--white);font-size:9.5px;line-height:19px;font-weight:700}
.support{left:748px;top:10px;width:194px;height:41px;background:#e7e5e5;display:flex}
.support-art{width:40px;height:41px;background:linear-gradient(#f0e4d8,#c9b8a6)}
.support-text{flex:1;text-align:center;font-size:7px;color:#777;padding-top:5px}
.support-text strong{display:block;font-size:12px;color:#666;margin-top:2px}

.intro{left:293px;top:332px;width:649px;height:60px;border:1px solid var(--line);text-align:center;padding-top:12px}
.intro p{font-size:9.5px}
.intro p+p{font-size:12.5px;margin-top:6px}

.special-offer{left:293px;top:402px;width:442px;height:94px;background:var(--offer)}
.special-offer h3{left:17px;top:16px;font-size:12px;line-height:15px;color:#c8c8c8;font-weight:700}
.special-offer p{left:17px;top:59px;width:100px;font-size:6px;line-height:10px;color:#bdbdbd;font-weight:700}
.offer-art{top:12px;height:66px;background:linear-gradient(135deg,#777,#111);border-radius:3px}
.offer-arrow{top:44px;width:0;height:0;border-top:4px solid transparent;border-bottom:4px solid transparent}

.about{left:293px;top:524px;width:442px;font-size:6.5px;line-height:9.8px;color:#444}

.info-card{top:623px;height:82px;background:var(--panel);padding:12px 12px;font-size:7px;color:#444}
.info-card h3{font-size:8px;font-weight:400;color:#333;margin-bottom:8px}
.info-card a{color:var(--orange);text-decoration:underline}
.tracking input{display:block;margin-top:12px;width:121px;height:21px;border:0;background:var(--white)}
.tracking button{position:absolute;left:135px;top:52px;width:65px;height:21px;border:0;background:var(--orange);font:700 7px "Arimo",Arial,sans-serif;color:#333}

.trust{left:748px;top:402px;width:194px;height:164px;border:1px solid var(--line);padding:10px 8px}
.trust h3{font-size:7.5px;text-align:center;line-height:11px;padding-bottom:6px;border-bottom:1px solid var(--line)}
.trust-badges{left:17px;top:44px;display:flex;flex-direction:column;gap:16px}
.badge-round{width:42px;height:42px;border-radius:50%;background:#e9d77a}
.badge-card{width:34px;height:16px;background:#c9d3e6;margin-left:4px}
.badge-card.alt{background:#f2c3a0}
.trust p{left:73px;top:46px;width:114px;font-size:6.3px;line-height:9.7px;color:#333}

.tags{left:748px;top:577px;width:194px;height:167px;border:1px solid var(--line);padding:14px 15px}
.tags h3{font-size:10px;font-weight:400;color:#666;padding-bottom:8px;border-bottom:1px solid var(--line);margin-bottom:6px}
.tags p{font-size:7.3px;line-height:19.5px;color:#999}
.tags .lg{font-size:10px;color:var(--orange)}
.tags .md{font-size:9px}
.tags .sm{font-size:5.5px}

.site-footer{position:absolute;left:0;top:764px;width:1200px;height:191px;background:var(--dark);color:#aaa}
.footer-col{top:34px}
.footer-col h4{font-size:10px;font-weight:400;color:var(--white);margin-bottom:14px}
.footer-col li{font-size:6.8px;line-height:13px}
.footer-col.tight li{line-height:10px}
.newsletter p{font-size:6.5px;margin-bottom:6px}
.newsletter form{display:flex}
.newsletter input{width:148px;height:21px;border:0;background:#444}
.newsletter button{width:46px;height:21px;border:0;background:var(--cyan);font:700 7px "Arimo",Arial,sans-serif;color:#222}

.legal{position:absolute;left:0;top:955px;width:1200px;height:45px;background:var(--darker);color:#ddd}
.legal-brand{left:485px;top:14px;display:flex;align-items:center;gap:3px;color:var(--yellow);font-size:8px;font-weight:700}
.legal-brand span{width:7px;height:7px;border-radius:50%;background:var(--yellow)}
.legal p{left:535px;top:15px;font-size:6.8px;line-height:11px;text-align:center}
</style>
</head>
<body>

<header class="site-header">
  <a class="brand abs" href="http://vantomere.com"><span class="brand-dot"></span>vantomere</a>
  <div class="cart abs">In Your Cart <b>(0)</b></div>
  <a class="proceed abs" href="#">Procede</a>
  <svg class="proceed-arrow abs" viewBox="0 0 20 19"><rect width="20" height="19" fill="#f7a01c"/><path d="M8 5l5 4.5L8 14" stroke="#fff" stroke-width="2" fill="none"/></svg>
  <nav class="main-nav abs">
    <a href="#">Résiliation Internet</a> &nbsp;| <a href="#">Résiliation Mobile</a> | <a href="#">Résiliation TV</a> | <a href="#">Résiliation Assurance</a> | <a href="#">Révoquer Prélevement</a> | <a href="#">Renvoyer Box Internet</a> | <a href="#">Renvoyer Décodeur TV</a>
  </nav>
</header>

<section class="services">
  <h2 class="abs">Choisissez le type de service à résilier</h2>
  <div class="slider-arrows abs"><span></span><span></span></div>
  <ul class="service-tiles abs">
    <li><div class="tile-art" role="img" aria-label="Smartphones mobiles"></div></li>
    <li><div class="tile-art" role="img" aria-label="Box internet Wi-Fi"></div></li>
    <li><div class="tile-art" role="img" aria-label="Téléviseur écran plat"></div></li>
    <li><div class="tile-art" role="img" aria-label="Famille sous un parapluie, assurance" style="background:linear-gradient(#555,#3aa0d8)"></div></li>
    <li><div class="tile-art" role="img" aria-label="Décodeur TV"></div></li>
    <li><div class="tile-art" role="img" aria-label="Ordinateur portable et lettre" style="background:linear-gradient(135deg,#cfd8e6,#2f5f9c)"></div></li>
  </ul>
  <p class="price abs">L'envoi de votre demande de résiliation coûte 7.70 €</p>
</section>

<section class="promise">
  <h1 class="abs">SERVICE D'ENVOI RECOMMANDE DE LETTRES DE DEMANDES DE RESILIATION<br>FIABLE, SIMPLE, RAPIDE ET SANS SE DEPLACER</h1>
  <div class="support abs">
    <div class="support-art" role="img" aria-label="Conseillère support avec casque"></div>
    <div class="support-text">Pour résilier ou joindre le support<br>Appelez le<strong>01 45 67 80 12 *</strong></div>
  </div>
</section>

<main>
  <div class="intro abs">
    <p>Utilisateurs mécontents ? Problèmes techniques ? Un déménagement ? Une offre concurrentielle alléchante ?</p>
    <p>N'attendez plus pour vous désabonner ! Désormais résilier rime avec simplicité, fiabilité, et efficacité !</p>
  </div>

  <section class="special-offer abs">
    <h3 class="abs">SPECIAL<br>OFFER</h3>
    <p class="abs">Lorem ipsum dolor sit amet, con sectetur adipiscing elit.</p>
    <span class="offer-arrow abs" style="left:148px;border-right:5px solid #bbb"></span>
    <div class="offer-art abs" role="img" aria-label="Smartphones" style="left:188px;width:70px"></div>
    <div class="offer-art abs" role="img" aria-label="Téléviseur" style="left:306px;width:72px;top:24px;height:44px"></div>
    <span class="offer-arrow abs" style="left:417px;border-left:5px solid #bbb"></span>
  </section>

  <article class="about abs">
    <p><strong>Vantomere.com</strong>, leader de l'envoi de lettre recommandée et de résiliation par internet, est la solution de choix pour tous les utilisateurs qui souhaitent se désabonner.</p>
    <p>Vantomere.com vous simplifie les démarches et les procédures de résiliation.</p>
    <p>Vantomere.com vous propose gratuitement, de multiples modèles de lettres de résiliation adaptés à chaque situation et à chaque besoin. Que ce soit pour résilier un contrat de téléphonie MOBILE ou fixe, un abonnement TV, ADSL, ASSURANCE, il existe un modèle de lettre personnalisable.</p>
    <p>Parce que nous savons que votre temps est précieux, vantomere.com vous permet d'envoyer votre lettre recommandée de résiliation avec accusé de réception sans vous déplacer.</p>
    <p>Pour chaque résiliation vous recevez une preuve de votre désabonnement, reconnue par la loi et les opérateurs.</p>
  </article>

  <section class="info-card abs" style="left:293px;width:213px">
    <h3>Information utile accessible en 1 clic</h3>
    <p>LES CONDITIONS GENERALES DE VENTE</p>
    <p style="margin-top:10px;line-height:10px">Retrouvez facilement toutes les <a href="#">conditions générales de ventes</a> des opérateurs en un clic.</p>
  </section>

  <section class="info-card tracking abs" style="left:518px;width:217px">
    <h3>Preuve et Suivi des envois</h3>
    <p style="line-height:10px">Saisissez le numéro à de votre courrier pour obtenir une preuve d'envoi et de réception :</p>
    <input type="text" aria-label="Numéro de courrier">
    <button type="submit">Envoyer</button>
  </section>

  <aside class="trust abs">
    <h3>Avec vantomere.com retrouvez votre liberté<br>de choisir en toute sécurité !</h3>
    <div class="trust-badges abs">
      <div class="badge-round"></div>
      <div class="badge-card"></div>
      <div class="badge-card alt"></div>
    </div>
    <p class="abs">Envoi de votre lettre de résiliation Mobile, Adsl, TV, en recommandé A/R Résiliation avec accusé de réception notifiée par voie postale. Signature électronique par Signalia. Interface de paiement sécurisée par carte (CSC/CVV2) vérifiée. Un litige avec un opérateur ? Appelez nos juristes au 01 45 67 80 34* Retrouvez-nous sur Socialis</p>
  </aside>

  <aside class="tags abs">
    <h3>Tag Links</h3>
    <p>résiliation, resiliation, RESILIATION, RESILIER, resilier, résilier, <span class="lg">resiliation abonnement</span>, résiliation abonnement, resiliation mobile, desa-bonnement, <span class="sm">resilier abonnement</span>, resiliation forfait, résiliation assurance, <span class="md">resiliation adsl</span>, résilia-tion adsl, resiliation internet</p>
  </aside>
</main>

<footer class="site-footer">
  <nav class="footer-col abs" style="left:293px">
    <h4>Products</h4>
    <ul><li>Résiliation Internet</li><li>Résiliation Mobile</li><li>Résiliation TV</li><li>Résiliation Assurance</li><li>Révoquer Prélevement</li><li>Renvoyer Box Internet</li><li>Renvoyer Décodeur TV</li></ul>
  </nav>
  <nav class="footer-col tight abs" style="left:457px">
    <h4>Site Info</h4>
    <ul><li>Lettre Recommandée</li><li>Modèle de lettre</li><li>Lettre-Type.net</li></ul>
  </nav>
  <nav class="footer-col tight abs" style="left:594px">
    <h4>About Us</h4>
    <ul><li>Lettre Recommandée</li><li>Modèle de lettre</li><li>Lettre-Type.net</li></ul>
  </nav>
  <div class="footer-col newsletter abs" style="left:748px">
    <h4>Newsletter</h4>
    <p>Lorem ipsum dolor sit amet, consectetur adipiscing elit</p>
    <form><input type="email" aria-label="Email"><button type="submit">Submit</button></form>
  </div>
</footer>

<div class="legal">
  <div class="legal-brand abs"><span></span>vantomere</div>
  <p class="abs">©Corvel Partners Ltd. 14, Ashbury Lane Harlow, CM1 7QX - Company 09127456<br>Brevet Recommandé A/R WO/2010/054321 | CGU | Cont@ct | Presse | Socialis</p>
</div>

</body>
</html>
```